Games for Classrooms Website Redesign

The purpose of the website redesign is to freshen up the content and update it to give a more modern look and feel. It will show what we do concisely and satisfy all potential visitors. We work with primary schools and the brand is fun.About: Games for Classrooms is a scheme that brings top Olympic athletes into primary schools to inspire children to do more physical activity. We typically run a half day event at the school where the athlete does a fun fitness circuit with the children and then an inspirational assembly with a demonstration and Q&A. The children are asked to collect sponsorship money to take part in the event and a large proportion of the money raised goes back to the school in the form of a voucher for them to spend on new sports equipment. 1. To generate more leads from potential customers/schools2. To engage the children and parents more in the event and get them excited for their upcoming visit whilst setting up a fundraiser page.3. To simplify and modernise what is already there.

I have attached some ideas for each of the pages (uploaded in brief)

Here is a link to our current website: www.gamesforclassrooms.org

I have also attached a link to the sponsorship form which shows the kind of look and feel we're after.

Target Market(s)

Primary school teachers
Primary school parents

Number of Pages Required

5+ page

Requirements
Must have
• Fun, modern.
• Be built on twitter bootstrap

```html
<!DOCTYPE html>
<html lang="en">
<head>
<meta charset="utf-8">
<title>Games for Classrooms</title>
<link href="https://fonts.googleapis.com/css2?family=Mulish:wght@400;600;700;800;900&display=swap" rel="stylesheet">
<style>
:root{
  --red:#e3171f;
  --navy:#2a3f86;
  --green:#4db848;
  --orange:#f1581d;
  --blue:#1e88e5;
  --text:#333a4d;
  --muted:#7a8194;
  --grey-bg:#e7e9f0;
  --card-bg:#eeeeee;
  --line:#9aa3bf;
  --footer:#1f1f22;
  --link:#2f8fd0;
}
*{box-sizing:border-box;margin:0;padding:0}
html,body{width:1200px;height:5248px;overflow:hidden}
body{font-family:"Mulish",Arial,sans-serif;color:var(--text);background:#fff;position:relative}
.abs{position:absolute}
section,header,footer{position:absolute;left:0;width:1200px}

/* header */
.site-header{top:0;height:98px;background:#fff}
.brand{left:144px;top:30px;display:flex;align-items:center;gap:10px}
.brand-dot{width:34px;height:34px;border-radius:50%;background:var(--red)}
.brand-name{font-weight:800;font-size:20px;color:var(--navy);letter-spacing:.3px}
.menu-btn{left:1015px;top:28px;width:42px;height:42px;background:#222;border-radius:3px;display:flex;flex-direction:column;justify-content:center;align-items:center;gap:4px}
.menu-btn i{display:block;width:16px;height:3px;background:#fff}

/* hero */
.hero{top:98px;height:525px;background:linear-gradient(135deg,#3d74b8 0%,#2f62a6 45%,#4c86c4 100%)}
.hero-title{top:50px;width:100%;text-align:center;color:#fff;font-weight:800;font-size:30px;letter-spacing:.5px}
.hero-text{top:92px;left:140px;width:920px;text-align:center;color:#fff;font-size:14px;line-height:1.55}
.hero-arrow{top:240px;width:20px;height:30px}
.hero-arrow.prev{left:45px}.hero-arrow.next{left:1130px}

/* role boxes */
.role-box{top:567px;width:441px;height:238px;color:#fff;text-align:center;padding-top:38px}
.role-box.school{left:144px;background:var(--green)}
.role-box.parent{left:616px;background:var(--orange)}
.role-box svg{display:block;margin:0 auto 8px}
.role-box h2{font-size:22px;font-weight:800;margin-bottom:10px}
.role-box p{font-size:11.5px;line-height:1.5;width:330px;margin:0 auto}

/* stats */
.stats{top:833px;height:80px}
.stat{position:absolute;top:0;width:150px;text-align:center}
.stat b{display:block;font-size:36px;font-weight:800;color:var(--navy);line-height:1.1}
.stat span{font-size:11px;color:var(--muted)}

/* common section */
.grey{background:var(--grey-bg)}
.section-title{top:0;width:100%;text-align:center;color:var(--red);font-weight:800;font-size:40px;letter-spacing:.5px}
.section-sub{width:920px;left:140px;text-align:center;color:var(--navy);font-weight:800;font-size:23px;line-height:1.45}

/* accordion */
.acc{left:144px;width:409px}
.acc-item{position:absolute;left:0;width:409px;border-bottom:2px solid var(--line);padding-bottom:12px}
.acc-q{display:flex;justify-content:space-between;align-items:flex-start;font-size:21px;font-weight:700;color:var(--navy);line-height:1.3}
.acc-q em{font-style:normal;flex:1;padding-right:20px}
.acc-ic{width:17px;height:17px;background:var(--navy);position:relative;margin-top:5px;flex:none}
.acc-ic::before,.acc-ic.plus::after{content:"";position:absolute;background:#fff}
.acc-ic::before{left:3px;top:7px;width:11px;height:3px}
.acc-ic.plus::after{left:7px;top:3px;width:3px;height:11px}
.acc-a{font-size:11px;line-height:1.5;color:var(--text);margin-top:10px}
.quote{position:absolute;left:0;width:409px;background:#fff;padding:22px 26px;font-size:13px;line-height:1.5;font-style:italic;color:var(--muted)}
.quote cite{display:block;font-style:normal;font-weight:700;color:var(--navy);margin-top:12px}

/* forms */
.right-col{left:633px;width:424px}
.field{position:absolute;left:0;width:424px;height:46px;background:#fff;border:1px solid #d3d6df;font-size:13px;color:#8a8f9c;padding:14px 22px}
.field.select::after{content:"";position:absolute;right:22px;top:19px;border:5px solid transparent;border-top:6px solid #555}
.find{position:absolute;left:0;font-size:17px;color:var(--green);font-weight:600}
.video{position:absolute;left:0;width:424px;background:linear-gradient(135deg,#7a6f6a,#b68e70 45%,#4f5a6c)}
.play{position:absolute;left:50%;top:50%;width:58px;height:58px;margin:-29px 0 0 -29px;border-radius:50%;background:#fff}
.play::after{content:"";position:absolute;left:23px;top:17px;border:12px solid transparent;border-left:17px solid #222;border-right:0}

/* steps */
.step{position:absolute;left:0;display:flex;align-items:center;gap:14px}
.step-ic{width:52px;height:52px;border-radius:50%;background:var(--green);display:flex;align-items:center;justify-content:center}
.step b{display:block;font-size:14px;color:var(--navy);font-weight:800}
.step span{font-size:14px;color:var(--navy);font-weight:700}

/* pillars */
.pillar{position:absolute;top:222px;width:220px;text-align:center}
.pillar-circle{width:132px;height:132px;border-radius:50%;background:var(--red);margin:0 auto;display:flex;flex-direction:column;align-items:center;justify-content:center;color:#fff;font-weight:800;font-size:21px;gap:6px}
.pillar p{font-size:10.5px;line-height:1.45;margin-top:50px;color:var(--text)}

/* educate */
.dl-btn{position:absolute;left:0;width:424px;height:52px;background:var(--blue);color:#fff;font-size:21px;font-weight:700;display:flex;align-items:center;justify-content:center;gap:10px}
.workshop{position:absolute;left:0;width:424px;background:linear-gradient(160deg,#6b5d5a,#3d3a44 60%,#5a4a46);display:flex;align-items:center;justify-content:center;text-align:center;color:#fff;font-size:22px;font-weight:700;line-height:1.3}

/* athletes */
.card{position:absolute;top:148px;width:297px;height:402px;background:var(--card-bg)}
.card-img{height:202px;background:linear-gradient(160deg,#5d8a4a,#a9b489 50%,#6a7a58);position:relative}
.card-badge{position:absolute;left:0;bottom:-2px;width:36px;height:36px;background:var(--link)}
.card-badge::after{content:"";position:absolute;left:13px;top:13px;width:10px;height:10px;border-radius:50%;background:#fff}
.card-text{padding:18px 22px 0 40px;font-size:14px;line-height:1.45;color:var(--link)}
.card-date{position:absolute;left:40px;top:368px;font-size:10.5px;color:#333}

/* footer */
.site-footer{top:5162px;height:86px;background:var(--footer)}
.copy{left:144px;top:36px;font-size:11px;color:#ccc}
.socials{left:788px;top:32px;display:flex;gap:4px}
.socials i{display:block;width:22px;height:22px;border-radius:50%}
</style>
</head>
<body>

<header class="site-header">
  <div class="brand abs"><span class="brand-dot"></span><span class="brand-name">Games for Classrooms</span></div>
  <div class="menu-btn abs"><i></i><i></i><i></i></div>
</header>

<section class="hero" role="img" aria-label="Photo of smiling children at a school sports event, tinted blue">
  <h1 class="hero-title abs">OUR MISSION</h1>
  <p class="hero-text abs">Phasellus nisl est, condimentum vitae faucibus in, sollicitudin vel metus. Nunc sit amet consequat risus. Curabitur ac elit leo, in eleifend dui tellus, in scelerisque est porttitor at. Integer eu massa lacinia, lacinia nulla non, volutpat purus. Sed libero felis, vestibulum et dolor sed, lacinia aliquet neque.</p>
  <svg class="hero-arrow prev abs" viewBox="0 0 20 30"><path d="M16 3 L4 15 L16 27" fill="none" stroke="#fff" stroke-width="4"/></svg>
  <svg class="hero-arrow next abs" viewBox="0 0 20 30"><path d="M4 3 L16 15 L4 27" fill="none" stroke="#fff" stroke-width="4"/></svg>
</section>

<div class="role-box school abs">
  <svg width="70" height="52" viewBox="0 0 70 52"><path d="M35 2 L50 14 H20 Z" fill="#fff"/><rect x="22" y="14" width="26" height="36" fill="#fff"/><rect x="4" y="24" width="18" height="26" fill="#fff"/><rect x="48" y="24" width="18" height="26" fill="#fff"/><rect x="31" y="36" width="8" height="14" fill="#4db848"/><rect x="9" y="30" width="7" height="6" fill="#4db848"/><rect x="54" y="30" width="7" height="6" fill="#4db848"/></svg>
  <h2>I'M A SCHOOL</h2>
  <p>Aenean sed quam non sapien faucibus vitae nec sit amet orci. Praesent quis risus at. In mollis nulla in pulvinar dictum.</p>
</div>
<div class="role-box parent abs">
  <svg width="70" height="52" viewBox="0 0 70 52"><circle cx="20" cy="10" r="8" fill="#fff"/><rect x="10" y="20" width="20" height="30" rx="4" fill="#fff"/><circle cx="48" cy="16" r="6" fill="#fff"/><rect x="40" y="24" width="16" height="26" rx="4" fill="#fff"/></svg>
  <h2>I'M A PARENT</h2>
  <p>Aenean sed quam non sapien faucibus vitae nec sit amet orci. Praesent quis risus at. In mollis nulla in pulvinar dictum.</p>
</div>

<section class="stats">
  <div class="stat" style="left:145px"><b>6254</b><span>Donec vestibulum odio</span></div>
  <div class="stat" style="left:296px"><b>324</b><span>Aenean feugiat</span></div>
  <div class="stat" style="left:450px"><b>82%</b><span>Donec sit amet</span></div>
  <div class="stat" style="left:597px"><b>12</b><span>Proin porta</span></div>
  <div class="stat" style="left:744px"><b>45158</b><span>Nullam accumsan</span></div>
  <div class="stat" style="left:901px"><b>481</b><span>Praesent elementum</span></div>
</section>

<!-- Parent -->
<section class="grey" style="top:980px;height:707px">
  <h2 class="section-title abs" style="top:64px">I'M A PARENT</h2>
  <div class="acc abs" style="top:165px">
    <div class="acc-item" style="top:0">
      <div class="acc-q"><em>What is the event?</em><span class="acc-ic"></span></div>
      <p class="acc-a">Phasellus nisl est, condimentum vitae faucibus in, sollicitudin vel metus. Nunc sit amet consequat risus. Curabitur ac elit leo, in eleifend dui tellus, in scelerisque est porttitor at. Integer eu massa lacinia, lacinia nulla non, volutpat purus.</p>
    </div>
    <div class="acc-item" style="top:145px">
      <div class="acc-q"><em>Why is it important?</em><span class="acc-ic plus"></span></div>
    </div>
    <div class="acc-item" style="top:216px">
      <div class="acc-q"><em>Where does the sponsorship money go?</em><span class="acc-ic plus"></span></div>
    </div>
    <blockquote class="quote" style="top:318px">" Nam et tortor in ante iaculis porttitor in luctus mi. Vivamus gravida sem a pretium euismod. Nam lobortis, purus et fringilla tempus, risus eros dignissim. "<cite>Sam Ridley</cite></blockquote>
  </div>
  <div class="right-col abs" style="top:171px">
    <div class="field" style="top:0">Find my school...</div>
    <p class="find" style="top:100px">Set up a fundraiser page in 3 simple steps</p>
    <div class="step" style="top:160px"><span class="step-ic"><svg width="22" height="22" viewBox="0 0 22 22"><rect x="2" y="4" width="14" height="14" fill="none" stroke="#fff" stroke-width="2"/><path d="M8 13 L19 2" stroke="#fff" stroke-width="3"/></svg></span><div><b>STEP - 1</b><span>Aenean sed quam non sapien faucibus</span></div></div>
    <div class="step" style="top:255px"><span class="step-ic"><svg width="18" height="22" viewBox="0 0 18 22"><path d="M1 1 H12 L17 6 V21 H1 Z" fill="#fff"/></svg></span><div><b>STEP - 2</b><span>Donec sit amet lectus nec mi tempor</span></div></div>
    <div class="step" style="top:350px"><span class="step-ic"><svg width="22" height="22" viewBox="0 0 22 22"><rect x="1" y="3" width="20" height="18" fill="#fff"/><rect x="1" y="3" width="20" height="5" fill="#2e7d32"/><rect x="5" y="11" width="4" height="3" fill="#4db848"/><rect x="12" y="11" width="4" height="3" fill="#4db848"/></svg></span><div><b>STEP - 3</b><span>Nullam accumsan purus vel tempus</span></div></div>
  </div>
</section>

<!-- School -->
<section style="top:1687px;height:525px;background:#fff">
  <h2 class="section-title abs" style="top:66px">I'M A SCHOOL</h2>
  <p class="section-sub abs" style="top:124px">Phasellus blandit quam a ipsum gravida dapibus. Cras sed augue tortor. Suspendisse elit ligula, iaculis dignissim justo eu, vestibulum venenatis elit.</p>
  <div class="pillar" style="left:145px"><div class="pillar-circle"><svg width="30" height="30" viewBox="0 0 30 30"><circle cx="15" cy="15" r="9" fill="none" stroke="#fff" stroke-width="6" stroke-dasharray="5 3"/><circle cx="15" cy="15" r="4" fill="#fff"/></svg>Activate</div><p>Aliquam malesuada eros sit amet luctus scelerisque maximus. Maecenas lobortis iaculis efficitur.</p></div>
  <div class="pillar" style="left:380px"><div class="pillar-circle"><svg width="30" height="30" viewBox="0 0 30 30"><path d="M5 4 H22 L26 8 V27 H9 L5 23 Z" fill="#fff"/><path d="M9 11 H22 M9 16 H22" stroke="#e3171f" stroke-width="2"/></svg>Educate</div><p>Aliquam malesuada eros sit amet luctus scelerisque maximus. Maecenas lobortis iaculis efficitur.</p></div>
  <div class="pillar" style="left:611px"><div class="pillar-circle"><svg width="30" height="30" viewBox="0 0 30 30"><rect x="3" y="13" width="6" height="14" fill="#fff"/><path d="M11 13 L17 3 C20 3 20 6 19 10 H26 C28 10 28 13 27 14 L24 27 H11 Z" fill="#fff"/></svg>Motivate</div><p>Aliquam malesuada eros sit amet luctus scelerisque maximus. Maecenas lobortis iaculis efficitur.</p></div>
  <div class="pillar" style="left:842px"><div class="pillar-circle"><svg width="30" height="30" viewBox="0 0 30 30"><circle cx="15" cy="12" r="9" fill="#fff"/><rect x="11" y="21" width="8" height="6" fill="#fff"/></svg>Innovate</div><p>Aliquam malesuada eros sit amet luctus scelerisque maximus. Maecenas lobortis iaculis efficitur.</p></div>
</section>

<!-- Activate -->
<section class="grey" style="top:2212px;height:819px">
  <h2 class="section-title abs" style="top:70px">ACTIVATE</h2>
  <p class="section-sub abs" style="top:134px">An athlete and whole school event that gets every child inspired &amp; excited about being active.</p>
  <div class="acc abs" style="top:245px">
    <div class="acc-item" style="top:0"><div class="acc-q"><em>What is it?</em><span class="acc-ic"></span></div><p class="acc-a">Phasellus nisl est, condimentum vitae faucibus in, sollicitudin vel metus. Nunc sit amet consequat risus. Curabitur ac elit leo, in eleifend dui tellus, in scelerisque est porttitor at. Integer eu massa lacinia, lacinia nulla non, volutpat purus.</p></div>
    <div class="acc-item" style="top:142px"><div class="acc-q"><em>Why is it important?</em><span class="acc-ic plus"></span></div></div>
    <div class="acc-item" style="top:212px"><div class="acc-q"><em>How much does it cost?</em><span class="acc-ic plus"></span></div></div>
    <div class="acc-item" style="top:282px"><div class="acc-q"><em>Who is it lectus to be?</em><span class="acc-ic plus"></span></div></div>
    <blockquote class="quote" style="top:350px">" Nam et tortor in ante iaculis porttitor in luctus mi. Vivamus gravida sem a pretium euismod. Nam lobortis, purus et fringilla tempus, risus eros dignissim. "<cite>Sam Ridley</cite></blockquote>
  </div>
  <div class="right-col abs" style="top:248px">
    <div class="video" style="top:0;height:210px" role="img" aria-label="Video still of children doing a fitness circuit in a school hall"><span class="play"></span></div>
    <p class="find" style="top:236px">Find out when we're next in your area..</p>
    <div class="field" style="top:282px">Name</div>
    <div class="field" style="top:338px">School</div>
    <div class="field" style="top:394px">Postcode</div>
    <div class="field select" style="top:450px">Best time to call</div>
  </div>
</section>

<!-- Educate -->
<section style="top:3031px;height:749px;background:#fff">
  <h2 class="section-title abs" style="top:70px">EDUCATE</h2>
  <p class="section-sub abs" style="top:134px">An athlete and whole school event that gets every child inspired &amp; excited about being active.</p>
  <div class="acc abs" style="top:250px">
    <div class="acc-item" style="top:0"><div class="acc-q"><em>What's involved?</em><span class="acc-ic"></span></div><p class="acc-a">Phasellus nisl est, condimentum vitae faucibus in, sollicitudin vel metus. Nunc sit amet consequat risus. Curabitur ac elit leo, in eleifend dui tellus, in scelerisque est porttitor at. Integer eu massa lacinia, lacinia nulla non, volutpat purus.</p></div>
    <div class="acc-item" style="top:142px"><div class="acc-q"><em>Why is it important?</em><span class="acc-ic plus"></span></div></div>
    <div class="acc-item" style="top:212px"><div class="acc-q"><em>How much?</em><span class="acc-ic plus"></span></div></div>
    <blockquote class="quote" style="top:282px;background:var(--grey-bg)">" Nam et tortor in ante iaculis porttitor in luctus mi. Vivamus gravida sem a pretium euismod. Nam lobortis, purus et fringilla tempus, risus eros dignissim. "<cite>Sam Ridley</cite></blockquote>
  </div>
  <div class="right-col abs" style="top:248px">
    <div class="dl-btn" style="top:0"><svg width="20" height="20" viewBox="0 0 20 20"><path d="M7 1 H13 V9 H18 L10 17 L2 9 H7 Z" fill="#fff"/><rect x="1" y="17" width="18" height="3" fill="#fff"/></svg>Download Top Tips</div>
    <div class="workshop" style="top:74px;height:347px" role="img" aria-label="Photo of an athlete running a classroom workshop with children">Find out more about our<br>workshops</div>
  </div>
</section>

<!-- Innovate -->
<section class="grey" style="top:3780px;height:752px">
  <h2 class="section-title abs" style="top:70px">INNOVATE</h2>
  <p class="section-sub abs" style="top:128px">We think school clubs should be fun to organise &amp; inspiring for kids</p>
  <div class="acc abs" style="top:178px">
    <div class="acc-item" style="top:0"><div class="acc-q"><em>What is it?</em><span class="acc-ic"></span></div><p class="acc-a">Phasellus nisl est, condimentum vitae faucibus in, sollicitudin vel metus. Nunc sit amet consequat risus. Curabitur ac elit leo, in eleifend dui tellus, in scelerisque est porttitor at. Integer eu massa lacinia, lacinia nulla non, volutpat purus.</p></div>
    <div class="acc-item" style="top:145px"><div class="acc-q"><em>Why is it important?</em><span class="acc-ic plus"></span></div></div>
    <div class="acc-item" style="top:215px"><div class="acc-q"><em>How much does it cost?</em><span class="acc-ic plus"></span></div></div>
    <div class="acc-item" style="top:285px"><div class="acc-q"><em>Who is it lectus to be?</em><span class="acc-ic plus"></span></div></div>
    <blockquote class="quote" style="top:358px">" Nam et tortor in ante iaculis porttitor in luctus mi. Vivamus gravida sem a pretium euismod. Nam lobortis, purus et fringilla tempus, risus eros dignissim. "<cite>Sam Ridley</cite></blockquote>
  </div>
  <div class="right-col abs" style="top:185px">
    <div class="video" style="top:0;height:207px" role="img" aria-label="Video still of children taking part in an after-school club"><span class="play"></span></div>
    <p class="find" style="top:236px">Find out when we're next in your area..</p>
    <div class="field" style="top:282px">Name</div>
    <div class="field" style="top:338px">School</div>
    <div class="field" style="top:394px">Postcode</div>
    <div class="field select" style="top:450px">Best time to call</div>
  </div>
</section>

<!-- Athletes -->
<section style="top:4532px;height:630px;background:#fff">
  <h2 class="section-title abs" style="top:66px">MEET THE ATHELETS</h2>
  <article class="card" style="left:144px"><div class="card-img" role="img" aria-label="Photo of an athlete playing football with children"><span class="card-badge"></span></div><p class="card-text">Fusce porta arcu mi, aliquet dictum nulla interdum quis. Donec quis mi congue, consequat ligula at, efficitur lacus lacinia quam</p><span class="card-date">16 January, 2019</span></article>
  <article class="card" style="left:452px"><div class="card-img" role="img" aria-label="Photo of an athlete posing with a group of pupils" style="background:linear-gradient(160deg,#a07a5c,#d9c3a4 50%,#6b6f86)"><span class="card-badge"></span></div><p class="card-text">Aliquam malesuada eros sit amet luctus scelerisque maximus. Maecenas lobortis iaculis efficitur. Nulla facilisi. Vestibulum venenatis elit.</p><span class="card-date">16 January, 2019</span></article>
  <article class="card" style="left:760px"><div class="card-img" role="img" aria-label="Photo of children racing on a school field" style="background:linear-gradient(160deg,#7b8e5a,#b9c49a 50%,#5b6b4a)"><span class="card-badge"></span></div><p class="card-text">Mauris pharetra eros lorem, vel egestas leo mattis eget. Donec a nisl vel ante tristique mollis nec sed odio. Praesent accumsan enim.</p><span class="card-date">16 January, 2019</span></article>
</section>

<footer class="site-footer">
  <p class="copy abs">Copyright © 2019 Games for Classrooms - All rights reserved.</p>
  <div class="socials abs">
    <i style="background:#3b5b98"></i><i style="background:#2fa8e0"></i><i style="background:#1f75b3"></i><i style="background:#d73d32"></i><i style="background:#c8232c"></i><i style="background:#e2482b"></i><i style="background:#d4302a"></i><i style="background:#6b7b8c"></i><i style="background:#3b7bbf"></i><i style="background:#58a942"></i>
  </div>
</footer>

</body>
</html>
```